BHAG Poster

We like creativity and visual boxes and shapes not just bullet points. We think we want it to be landscape view. Here are some of the parameters:

BHAG:
Become one of the most admired construction companies in the markets we serve within the next 10 years

3 – 5 year goals:
1. Generate 35m in revenue by 2020
2. Have a 50/50 mix of Public-Private job mix
3. Maintain 15% annual growth

1 year goals:
1. $24M in revenue with better margins
2. 14% gross margin on year
3. Business development begins to pay off
4. Continue recruiting great & talented people

Dynamic Quarter Goal:
(Leave this area blank so we can fill it in each quarter please)

Industry/Entity Type

Landscape

Colors
0355a3

Requirements
Must have
• SHAPES OR BOXES FOR VISUAL EFFECT. We don't want it to just be words on a page. Must be creative. Must have our logo somewhere on the poster. Our cmyk blue color is 100-80-0-22. Poster can have different colors, but it just needs to have some of our blue in it.
Should not have
• no bullet points

```html
<!DOCTYPE html>
<html lang="en">
<head>
<meta charset="utf-8">
<title>BHAG Poster – Halden Construction</title>
<link href="https://fonts.googleapis.com/css2?family=Bebas+Neue&family=Source+Sans+3:wght@400;600;700&display=swap" rel="stylesheet">
<style>
  :root{
    --backdrop:#5b5b5b;
    --brand-blue:#2343a0;
    --card-blue:#2342a0;
    --ink:#111111;
    --text-dark:#1d1d1d;
    --footer-dark:#2c2c2c;
    --paper:#ffffff;
  }
  *{box-sizing:border-box;margin:0;padding:0}
  html,body{width:1200px;height:1200px;overflow:hidden}
  body{background:var(--backdrop);font-family:"Source Sans 3",sans-serif;position:relative}

  .poster{
    position:absolute;left:66px;top:223px;width:1068px;height:754px;overflow:hidden;
    background:linear-gradient(135deg,#f4f4f4 0%,#e2e2e2 35%,#c9c9c9 70%,#bdbdbd 100%);
    box-shadow:0 6px 14px rgba(0,0,0,.45);
  }
  .poster-stripes{position:absolute;inset:0}
  .city-haze{
    position:absolute;left:0;right:0;top:300px;height:360px;
    background:linear-gradient(180deg,rgba(255,255,255,0) 0%,rgba(235,235,235,.55) 40%,rgba(200,200,200,.6) 100%);
  }
  .site-photo{position:absolute;left:0;top:0;width:1068px;height:330px}

  .bhag{position:absolute;left:74px;top:52px;color:var(--text-dark)}
  .bhag-title{font-family:"Bebas Neue",sans-serif;font-size:52px;line-height:1;color:var(--brand-blue);letter-spacing:.5px}
  .bhag-statement{font-weight:400;font-size:27px;line-height:34px;margin-top:6px}
  .bhag-statement strong{font-weight:700}

  .goal-card{position:absolute;top:276px;width:290px;height:346px}
  .goal-card--long{left:46px}
  .goal-card--short{left:374px}
  .goal-head{
    position:absolute;left:20px;top:2px;width:268px;height:94px;background:var(--ink);
    border-radius:0 8px 0 0;
  }
  .goal-head::after{content:"";position:absolute;right:0;bottom:-6px;width:10px;height:6px;background:#0d1f5c}
  .goal-title{
    position:absolute;left:92px;top:35px;font-family:"Bebas Neue",sans-serif;font-size:25px;line-height:1;
    color:var(--paper);letter-spacing:.2px;white-space:nowrap;font-weight:400
  }
  .goal-title b{font-size:30px;font-weight:400}
  .goal-card--short .goal-title{left:124px}
  .goal-badge{position:absolute;left:0;top:0;width:98px;height:98px}
  .goal-body{
    position:absolute;left:34px;top:90px;width:242px;height:256px;background:var(--card-blue);
    padding:14px 4px 0 10px;box-shadow:0 10px 12px -6px rgba(0,0,0,.35)
  }
  .goal-list{list-style:none}
  .goal-item{display:flex;gap:8px;color:var(--paper);font-size:18.5px;line-height:24.5px;margin-bottom:16px}
  .goal-card--short .goal-item{margin-bottom:8px}
  .goal-marker{flex:none;width:15px;height:15px;margin-top:5px;background:linear-gradient(135deg,#ffffff,#b8c6ee);border:1px solid #8ea2dc}

  .quarter-box{position:absolute;left:708px;top:346px;width:301px;height:272px;background:var(--paper)}
  .quarter-edge{position:absolute;left:0;width:100%;height:10px}
  .quarter-edge--top{top:0}
  .quarter-edge--bottom{bottom:0}
  .quarter-title{
    position:absolute;top:36px;width:100%;text-align:center;font-family:"Bebas Neue",sans-serif;
    font-size:26px;font-weight:400;color:var(--brand-blue)
  }

  .footer{position:absolute;left:0;top:654px;width:1068px;height:100px}
  .footer-shapes{position:absolute;inset:0}
  .call{position:absolute;left:71px;top:5px}
  .call-label{font-weight:700;font-size:20px;color:var(--text-dark);letter-spacing:.3px}
  .call-number{font-family:"Bebas Neue",sans-serif;font-size:42px;line-height:1;color:var(--brand-blue);margin-top:-2px;letter-spacing:.5px}
  .contact{position:absolute;left:390px;top:20px;color:var(--paper);font-size:13.5px}
  .contact-row{display:flex;align-items:center;gap:8px;margin-bottom:9px;white-space:nowrap}
  .contact-row svg{flex:none}
  .brand{position:absolute;left:820px;top:30px;display:flex;align-items:center;gap:8px}
  .brand-square{width:34px;height:34px;background:var(--ink)}
  .brand-name{font-family:"Bebas Neue",sans-serif;font-size:26px;line-height:1;color:var(--ink);white-space:nowrap}
</style>
</head>
<body>
<main class="poster">
  <svg class="poster-stripes" width="1068" height="754" aria-hidden="true">
    <polygon points="120,0 300,0 700,754 520,754" fill="#ffffff" opacity=".18"/>
    <polygon points="380,0 470,0 870,754 780,754" fill="#ffffff" opacity=".14"/>
    <polygon points="-100,120 0,120 330,754 230,754" fill="#ffffff" opacity=".12"/>
  </svg>
  <div class="city-haze" role="img" aria-label="Faint line drawing of a city skyline behind the goal cards"></div>

  <svg class="site-photo" width="1068" height="330" role="img" aria-label="Blue-toned photo of workers in hard hats in front of a building under construction">
    <defs>
      <linearGradient id="siteTone" x1="0" y1="0" x2="1" y2="1">
        <stop offset="0" stop-color="#9fb0ee"/>
        <stop offset=".45" stop-color="#2f4fd0"/>
        <stop offset="1" stop-color="#081a6a"/>
      </linearGradient>
    </defs>
    <polygon points="482,0 1068,0 1068,329 778,329" fill="url(#siteTone)"/>
    <line x1="778" y1="329" x2="1068" y2="329" stroke="#8c7a3c" stroke-width="2"/>
  </svg>

  <header class="bhag">
    <h1 class="bhag-title">BHAG</h1>
    <p class="bhag-statement">Become one of the most admired<br>construction companies in the markets<br>we serve within the next <strong>10 years</strong></p>
  </header>

  <section class="goal-card goal-card--long">
    <div class="goal-head"><h2 class="goal-title"><b>3</b> - <b>5</b> Year Goals</h2></div>
    <svg class="goal-badge" viewBox="0 0 98 98" aria-hidden="true">
      <circle cx="49" cy="49" r="49" fill="#111"/>
      <circle cx="52" cy="49" r="40" fill="#fff"/>
      <circle cx="52" cy="49" r="27" fill="none" stroke="#3a5bd0" stroke-width="6"/>
      <circle cx="52" cy="49" r="15" fill="none" stroke="#3a5bd0" stroke-width="5"/>
      <circle cx="52" cy="49" r="5" fill="#3a5bd0"/>
      <line x1="52" y1="49" x2="30" y2="27" stroke="#1b2f7a" stroke-width="3"/>
      <polygon points="26,22 34,24 28,30" fill="#1b2f7a"/>
    </svg>
    <div class="goal-body">
      <ul class="goal-list">
        <li class="goal-item"><span class="goal-marker"></span><span>Generate 35m in<br>revenue by 2020</span></li>
        <li class="goal-item"><span class="goal-marker"></span><span>Have a 50/50 mix of<br>Public-Private job mix</span></li>
        <li class="goal-item"><span class="goal-marker"></span><span>Maintain 15% annual<br>growth</span></li>
      </ul>
    </div>
  </section>

  <section class="goal-card goal-card--short">
    <div class="goal-head"><h2 class="goal-title"><b>1</b> Year Goals</h2></div>
    <svg class="goal-badge" viewBox="0 0 98 98" aria-hidden="true">
      <circle cx="49" cy="49" r="49" fill="#111"/>
      <circle cx="52" cy="49" r="40" fill="#fff"/>
      <circle cx="52" cy="49" r="27" fill="none" stroke="#3a5bd0" stroke-width="6"/>
      <circle cx="52" cy="49" r="15" fill="none" stroke="#3a5bd0" stroke-width="5"/>
      <circle cx="52" cy="49" r="5" fill="#3a5bd0"/>
      <line x1="52" y1="49" x2="30" y2="27" stroke="#1b2f7a" stroke-width="3"/>
      <polygon points="26,22 34,24 28,30" fill="#1b2f7a"/>
    </svg>
    <div class="goal-body">
      <ul class="goal-list">
        <li class="goal-item"><span class="goal-marker"></span><span>$24M in revenue with<br>better margins</span></li>
        <li class="goal-item"><span class="goal-marker"></span><span>14% gross margin on<br>year</span></li>
        <li class="goal-item"><span class="goal-marker"></span><span>Business development<br>begins to pay off</span></li>
        <li class="goal-item"><span class="goal-marker"></span><span>Continue recruiting<br>great &amp; talented people</span></li>
      </ul>
    </div>
  </section>

  <section class="quarter-box">
    <svg class="quarter-edge quarter-edge--top" viewBox="0 0 301 10" preserveAspectRatio="none" aria-hidden="true">
      <rect width="301" height="10" fill="#111"/>
      <line x1="0" y1="5" x2="301" y2="5" stroke="#fff" stroke-width="4" stroke-dasharray="8 6"/>
    </svg>
    <h2 class="quarter-title">Dynamic Quarter Goal</h2>
    <svg class="quarter-edge quarter-edge--bottom" viewBox="0 0 301 10" preserveAspectRatio="none" aria-hidden="true">
      <rect width="301" height="10" fill="#111"/>
      <line x1="0" y1="5" x2="301" y2="5" stroke="#fff" stroke-width="4" stroke-dasharray="8 6"/>
    </svg>
  </section>

  <footer class="footer">
    <svg class="footer-shapes" width="1068" height="100" aria-hidden="true">
      <rect x="0" y="0" width="1068" height="100" fill="#fff"/>
      <rect x="0" y="79" width="785" height="21" fill="#2c2c2c"/>
      <polygon points="334,0 738,0 785,100 362,100 352,79 334,0" fill="#2c2c2c"/>
      <polygon points="334,0 352,79 362,79" fill="#fff"/>
    </svg>
    <div class="call">
      <p class="call-label">CALL US NOW</p>
      <p class="call-number">555.014.2290</p>
    </div>
    <div class="contact">
      <p class="contact-row">
        <svg width="16" height="14" viewBox="0 0 16 14" aria-hidden="true"><path d="M8 0 L16 7 H13 V14 H9.5 V9.5 H6.5 V14 H3 V7 H0 Z" fill="#fff"/></svg>
        820 Foundry Lane Riverton, Mississippi 39000
      </p>
      <p class="contact-row">
        <svg width="16" height="16" viewBox="0 0 16 16" aria-hidden="true"><g fill="none" stroke="#fff" stroke-width="1.3"><circle cx="8" cy="8" r="6.5"/><ellipse cx="8" cy="8" rx="3" ry="6.5"/><line x1="1.5" y1="8" x2="14.5" y2="8"/></g></svg>
        www.haldenbuild.com
      </p>
    </div>
    <div class="brand">
      <span class="brand-square"></span>
      <span class="brand-name">Halden Construction</span>
    </div>
  </footer>
</main>
</body>
</html>
```